Design some Business Cards for Real Estate Company

This is the contest I ran last year. I like #176
https://www.briefgallop.example/contest/Design-Business-Card-for-NYC-Real-Estate-Firm-83917.html

Looking for:
Clean, sexy, chic card
One side white
Horizontal

*DON'T: write "email" or "phone" - Don't have a picture of phone or email sign*

FRONT OF THE CARD: If you want to put a logo, have it watermarked
COLOR: see attached
NAME: Miriam Faye Quillerby, Founder
SMALL FONT SIZE: Licensed Real Estate Broker
ADDRESS: 4806 Larkspur Boulevard, 17th Floor, New York, New York 10036
EMAIL: miriam@[url removed, login to view]
WEBSITE (don't include www): [url removed, login to view]
PHONE: c 212.555.7314 (include the 'c' for cell)
PHONE: o 212.555.9062 (include the 'o' for office)
SOCIAL
[url removed, login to view]

BACK OF THE CARD
LOGO: see attached (horizontal)
CENTERED TEXT: Investing | Brokerage | New Development | Management

```html
<!DOCTYPE html>
<html lang="en">
<head>
<meta charset="utf-8">
<title>Quillerby Properties International – Business Card</title>
<link rel="stylesheet" href="https://fonts.googleapis.com/css2?family=Cinzel:wght@400;500&display=swap">
<style>
  :root {
    --page-bg: #e9e7e3;
    --card-bg: #ffffff;
    --accent: #2aa6d6;
    --ink: #2b2b2b;
    --muted: #6d6d6d;
    --shadow: rgba(0, 0, 0, 0.18);
  }
  * { margin: 0; padding: 0; box-sizing: border-box; }
  html, body {
    width: 1200px;
    height: 1023px;
    overflow: hidden;
    background: var(--page-bg);
  }
  .canvas {
    position: relative;
    width: 1200px;
    height: 1023px;
  }
  .card {
    position: absolute;
    left: 100px;
    top: 226px;
    width: 1000px;
    height: 571px;
    background: linear-gradient(180deg, #ffffff 0%, #f6f6f6 100%);
    box-shadow: 0 12px 40px var(--shadow);
    font-family: "Cinzel", serif;
    text-transform: uppercase;
  }
  .rule {
    position: absolute;
    left: 0;
    right: 0;
    top: 262px;
    height: 2px;
    background: var(--accent);
  }
  .brand { position: absolute; left: 50px; top: 206px; }
  .brand-name {
    font-size: 42px;
    font-weight: 400;
    letter-spacing: 2px;
    color: var(--accent);
    line-height: 1;
  }
  .brand-tagline {
    margin-top: 22px;
    font-size: 14px;
    letter-spacing: 2.5px;
    color: var(--muted);
  }
  .person { position: absolute; left: 450px; top: 214px; }
  .person-name {
    font-size: 30px;
    letter-spacing: 1.5px;
    color: var(--ink);
    line-height: 1;
  }
  .person-role {
    margin-top: 28px;
    font-size: 14px;
    letter-spacing: 1.5px;
    color: var(--accent);
    line-height: 22px;
  }
  .address {
    margin-top: 14px;
    font-size: 13px;
    letter-spacing: 1px;
    color: var(--muted);
    line-height: 22px;
  }
  .contact {
    position: absolute;
    right: 50px;
    top: 392px;
    text-align: right;
    font-size: 13px;
    letter-spacing: 1px;
    color: var(--muted);
    line-height: 23px;
  }
  .social {
    position: absolute;
    left: 50px;
    top: 392px;
    list-style: none;
    font-size: 12px;
    letter-spacing: 1px;
    color: var(--muted);
  }
  .social li {
    display: flex;
    align-items: center;
    height: 30px;
  }
  .social-dot {
    width: 18px;
    height: 18px;
    border-radius: 50%;
    background: var(--accent);
    margin-right: 12px;
    flex: none;
  }
</style>
</head>
<body>
<main class="canvas">
  <section class="card" aria-label="Business card front">
    <div class="rule"></div>

    <div class="brand">
      <div class="brand-name">Quillerby</div>
      <div class="brand-tagline">Properties International</div>
    </div>

    <div class="person">
      <div class="person-name">Miriam Faye Quillerby</div>
      <div class="person-role">Founder<br>Licensed Real Estate Broker</div>
      <div class="address">4806 Larkspur Boulevard, 17th Floor<br>New York, New York 10036</div>
    </div>

    <ul class="social">
      <li><span class="social-dot"></span>snapfolio.example/qpinyc</li>
      <li><span class="social-dot"></span>viewreel.example/qpinyc</li>
      <li><span class="social-dot"></span>friendwall.example/qpinyc</li>
    </ul>

    <div class="contact">
      C. 212.555.7314<br>
      O. 212.555.9062<br>
      miriam@quillerbyprop.example<br>
      quillerbyprop.example
    </div>
  </section>
</main>
</body>
</html>
```